Professional Price List Design for Luxury Candle Range (Print-Ready)

This project requires a luxury, calm, high-end price list — not a flyer, not a basic price sheet. I am wanting mainly soft whites, warm creams, beige, subtle gold tones - no bold colours. Layout to be clearly sectioned by candle range; each range must read as a distinct feature, while flowing cohesively on one page (ideally without looking cramped).
Use clean margins and balanced spacing.
Overall layout should resemble a boutique catalogue or luxury menu
Use some of the supplied candle images only, true to size (no distortion)
Elegant, refined typography is essential

If this style or level of refinement is not aligned with your design approach, please do not submit an entry.

Target Market(s)

Individuals interested in wellness, mindfulness, and soulful living

Industry/Entity Type

Wellness & Lifestyle Brand

Colors

Designer to choose colors to be used in the design.

Requirements
Must have
• A design that allows for future updates as new products are released. Contact email clearly visible for ordering
Nice to have
• Some snap shots of each different candle ranges - I have attached individual photos to brief - they DO NOT all have to be included, they are just examples in case you want to use them.
Should not have
• No loud colours. No crowded pricing or tight spacing.

```html
<!DOCTYPE html>
<html lang="en">
<head>
<meta charset="utf-8">
<title>Kindred Wick — Price List</title>
<link href="https://fonts.googleapis.com/css2?family=Cinzel:wght@400;600;700&family=Arimo:wght@400;700&display=swap" rel="stylesheet">
<style>
  :root {
    --backdrop: #534a48;
    --paper: #ffffff;
    --olive: #5e6b2a;
    --ink: #3a2f2a;
    --rule: #4a3f3a;
  }
  * { margin: 0; padding: 0; box-sizing: border-box; }
  html, body { width: 1200px; height: 1200px; overflow: hidden; }
  body { background: var(--backdrop); position: relative; font-family: "Arimo", Helvetica, Arial, sans-serif; color: var(--ink); }
  .sheet { position: absolute; left: 239px; top: 90px; width: 722px; height: 1020px; background: var(--paper); }
  .sheet-title {
    position: absolute; left: 60px; top: 54px;
    font-family: "Cinzel", serif; font-weight: 400; font-size: 26px; letter-spacing: 1px; color: var(--olive);
  }
  .brand-corner {
    position: absolute; right: 62px; top: 62px;
    font-family: "Cinzel", serif; font-weight: 700; font-size: 13px; letter-spacing: 1px; color: var(--olive);
  }
  .rule { position: absolute; left: 60px; width: 603px; height: 1px; background: var(--rule); }
  .rule-top { top: 108px; }
  .rule-bottom { top: 848px; }
  .column { position: absolute; top: 125px; width: 287px; }
  .column-left { left: 60px; }
  .column-right { left: 377px; }
  .range-name {
    font-family: "Cinzel", serif; font-weight: 700; font-size: 19px; line-height: 19.5px;
    letter-spacing: 0.5px; color: var(--olive); margin-bottom: 8px;
  }
  .range-intro { font-size: 11.6px; line-height: 14.6px; margin-bottom: 9px; }
  .price-list { list-style: none; }
  .price-list li {
    display: flex; justify-content: space-between; align-items: flex-end;
    font-weight: 700; font-size: 11.6px; line-height: 14.6px; color: var(--olive);
  }
  .divider { width: 22px; height: 1px; background: var(--rule); margin: 14px 0 14px; }
  .note { font-size: 11.6px; line-height: 14.6px; margin-bottom: 13px; }
  .brand-footer {
    position: absolute; left: 0; width: 100%; top: 893px; text-align: center;
    font-family: "Arimo", sans-serif; font-weight: 400; color: var(--olive);
  }
  .brand-footer .brand-main { display: block; font-size: 46px; line-height: 50px; letter-spacing: 4px; }
  .brand-footer .brand-sub { display: block; font-size: 26px; line-height: 30px; letter-spacing: 5px; }
</style>
</head>
<body>
  <main class="sheet">
    <h1 class="sheet-title">PRICE LIST</h1>
    <div class="brand-corner">KINDRED WICK</div>
    <div class="rule rule-top"></div>

    <section class="column column-left">
      <h2 class="range-name">HERITAGE<br>LUXURY<br>RANGE</h2>
      <p class="range-intro">Set in graceful, generous vessels, the Heritage Luxury Range offers classic jars made to fill your home with glow, ease, and understated elegance.</p>
      <ul class="price-list"><li><span>Velvet Riviera • Grand Jar • 400g</span><span>$50</span></li></ul>
      <div class="divider"></div>

      <h2 class="range-name">SIGNATURE<br>AFFIRMATION<br>RANGE</h2>
      <p class="range-intro">Each candle carries a quiet message - a soft nudge. Toward rest. Toward courage. Toward making room for the small moments that restore you. Made to invite stillness, inner listening, and mindful days.</p>
      <ul class="price-list">
        <li><span>Halden Amber Jar • Oak Lid • 295g</span><span>$30</span></li>
        <li><span>Opal Dome Jar • 200g</span><span>$40</span></li>
      </ul>
      <div class="divider"></div>

      <h2 class="range-name">DAILY<br>RITUALS</h2>
      <p class="range-intro">Easy, cosy candles made for the small everyday pauses of rest and comfort.</p>
      <ul class="price-list"><li><span>Classic Amber • 150g</span><span>$20</span></li></ul>
      <div class="divider"></div>

      <h2 class="range-name">SWEET<br>TREAT<br>RANGE</h2>
      <p class="range-intro">A playful, dessert-inspired collection that looks tempting enough to taste and smells wonderfully rich. The Sweet Treat Collection wraps your room in warm, cosy notes — a little fragrant indulgence.</p>
      <ul class="price-list">
        <li><span>Vanilla Shake • 235g</span><span>$35</span></li>
        <li><span>Cocoa Shake • 235g</span><span>$35</span></li>
        <li><span>Toffee Crunch • 295g</span><span>$30</span></li>
        <li><span>Mocha Cream • 295g</span><span>$30</span></li>
        <li><span>Honey Latte • 295g</span><span>$30</span></li>
      </ul>
    </section>

    <section class="column column-right">
      <h2 class="range-name">NEWBORN<br>&amp; MEMORY<br>RANGE</h2>
      <p class="range-intro">Made to mark a new arrival, this range offers a tender greeting to the world. Calm, heartfelt candles created to honour family, fresh starts, and the joy each tiny one brings.</p>
      <ul class="price-list">
        <li><span>Hello, Tiny One •<br>Halden Bowl Candle</span><span>$55</span></li>
        <li><span>Hello, Tiny One •<br>Halden Large Jar • 400g</span><span>$40</span></li>
      </ul>
      <div class="divider"></div>

      <h2 class="range-name">SEASONAL<br>RELEASE<br>RANGE</h2>
      <p class="range-intro">Hand-poured candles made in small runs and offered for a brief season only.</p>
      <ul class="price-list">
        <li><span>Blush Petals • 200g</span><span>$30</span></li>
        <li><span>Forever Yours • Seasonal • 400g</span><span>$40</span></li>
        <li><span>Cuddle Cove • Halden Bowl Candle</span><span>$55</span></li>
      </ul>
      <div class="divider"></div>

      <p class="note">Kindred Wick is a growing collection. Fresh candle designs are added often, and this price list may change from time to time to include new pieces and seasonal releases.</p>
      <p class="note">Every Kindred Wick candle is made gently and with care, with purpose at its heart - because the things we welcome into our homes, and our days, really count.</p>
      <p class="note">Our online shop is on its way. Web ordering will open shortly. Until then, every order can be arranged by reaching us by email at hello@kindredwick.com.</p>
    </section>

    <div class="rule rule-bottom"></div>
    <div class="brand-footer">
      <span class="brand-main">KINDRED</span>
      <span class="brand-sub">WICK</span>
    </div>
  </main>
</body>
</html>
```